IT company website design

Require a home page and an inner page designed for a company located in Ohio. The company deals with a wide range of IT services like Software development, IT based education services such as digital textbooks and BPO

Would like to get a Home page for the website and an inner page to be designed.

Design must be modern, clean and very professional. The home page should have a carousel of our services for which content will be provided.

It should give a feel that we are a large company to our prospective customers.
Updates

Hi,
In the few designs I have got for the home page, there are mockups with unwanted content/blocks like ex. latest blog posts or similar blocks. Kindly note that, we don't want this. Please follow the information about content on the home page as mentioned in the project brief. Designers, who have already submitted designs, if you can remove the unwanted blocks, it will be really appreciated.

Thanks.

I have received over 9 designs for this project, but none of them seem to be custom designed for my needs. They are just re-use of previous designs and look very out dated. Looking for fresh, clean designs following latest design trends like the ones you see in gridmarket etc.

If you can provide me a design that meets my expectations, I can definitely UP my budget for you .

Industry/Entity Type

Education

Requirements
Must have
• > > Home page > >
Home page will have

* Top Menu: Home, About Us, Solutions, Services, Contact us (should have space to accommodate for more)

* Should have a flash carousel/slide show. Each slide should be about a service we provide. Ex. a slide for bpo will have the content "Bridging the quality and cost divide in outsourcing" It should be depicted by an illustration or photograph. If you are going to use photograph, please use ones for pixvaultimages.com

* Textual content of about 200 words which we will provide

* Links in the footer along with a copyright, legal notice etc.

* Importantly, the home page should have 2 fancy buttons for "Member Login" and "Online Tutoring"

> > Inner pages > >
Will be mainly textual content explaining each of the service so, should have space for lots of textual content, with a fancy, page title (usually the service name). All inner pages should also have a side menu or something like that from where users can have a one click access to all our services.

Our logo is blue in color. with color code "0080FB". It just a stylized D with rest of the text i.e Varnex Tek Inc. our logo is of the proportion. 1:5 i.e 60px height, 300px wide. We can proportionately increase or decrease the dimensions as necessary. Color combination of the sight should be something that will go with this.

```html
<!DOCTYPE html>
<html lang="en">
<head>
<meta charset="utf-8">
<title>Varnex Tek Inc. — Home</title>
<link rel="stylesheet" href="https://fonts.googleapis.com/css2?family=Open+Sans:wght@400;600;700&family=Comfortaa:wght@700&display=swap">
<style>
  :root{
    --page-bg:#323a47;
    --page-bg-light:#3b4453;
    --band-dark:#242a33;
    --panel-dark:#232a34;
    --panel-login:#1c2129;
    --nav-bg:#2a313c;
    --nav-link:#1e90e6;
    --tab-light:#d9dadd;
    --logo-bg:#d4d5d9;
    --logo-text:#2f3238;
    --brand-blue:#0080fb;
    --body-text:#a8e2e6;
    --lead-text:#5aa6e4;
    --heading:#ffffff;
    --field-bg:#c9cbcf;
    --field-text:#6a6d72;
    --orange-top:#ffa21f;
    --orange-bottom:#e65d00;
    --footer-bg:#3a4250;
    --footer-text:#a3a8b0;
  }
  *{box-sizing:border-box;margin:0;padding:0}
  html,body{width:1200px;height:1200px;overflow:hidden;background:var(--page-bg)}
  body{font-family:Arial,"Open Sans",sans-serif}
  .page{position:relative;width:1200px;height:1200px;
    background:linear-gradient(180deg,var(--page-bg) 0,var(--page-bg-light) 280px,var(--page-bg) 600px,#2b323d 1130px)}
  .abs{position:absolute}

  .nav{left:392px;top:0;width:808px;height:65px;background:linear-gradient(180deg,#353d49,var(--nav-bg));
    border-bottom:3px solid #c8cbd0}
  .nav a{position:absolute;top:0;height:65px;line-height:65px;font-family:"Open Sans",sans-serif;
    font-size:18px;color:var(--nav-link);text-decoration:none;transform:translateX(-50%)}
  .nav .home{left:0;width:124px;transform:none;text-align:center;font-weight:700;color:#2b2e33;
    background:linear-gradient(180deg,#eeeff1,var(--tab-light))}

  .logo{left:0;top:0;width:392px;height:145px;background:linear-gradient(180deg,#e9eaec,var(--logo-bg));
    border-radius:0 0 4px 0;box-shadow:0 3px 8px rgba(0,0,0,.45);display:flex;align-items:center;padding-left:40px;gap:14px}
  .logo .mark{width:28px;height:28px;background:var(--brand-blue)}
  .logo .name{font-family:"Open Sans",sans-serif;font-size:44px;color:var(--logo-text);letter-spacing:-1px}

  .search{left:887px;top:83px;width:241px;height:29px;border-radius:4px;background:linear-gradient(180deg,#bfc1c5,#d8d9dc);
    border:1px solid #8a8d92;font-size:14px;color:#777;padding:5px 8px}
  .search-icon{left:1132px;top:80px}
  .social{top:124px;width:42px;height:42px;border-radius:7px;box-shadow:0 1px 3px rgba(0,0,0,.5)}

  .band{left:0;top:282px;width:1200px;height:190px;background:var(--band-dark);
    border-top:1px solid #444c59;border-bottom:1px solid #444c59}

  .slider{left:174px;top:204px;width:853px;height:366px;border-radius:5px;padding:8px 16px 10px;
    background:linear-gradient(180deg,#f2f3f4,#b8bbc0);box-shadow:0 2px 8px rgba(0,0,0,.5)}
  .slide{display:flex;width:100%;height:100%;border-radius:3px;overflow:hidden}
  .slide .half{flex:1;height:100%}
  .slide .left{background:linear-gradient(180deg,#e3e0c6 0%,#b9b49a 55%,#6d7488 100%)}
  .slide .right{background:linear-gradient(180deg,#d9e4e4 0%,#a9c1c4 50%,#a2809c 100%);border-left:4px solid #fff}

  .content{left:46px;top:606px;width:814px;height:526px;background:var(--panel-dark)}
  .content h1{position:absolute;left:87px;top:38px;font-family:"Open Sans",sans-serif;font-size:22px;font-weight:700;color:var(--heading)}
  .content .bullet{position:absolute;left:45px;top:42px}
  .content .lead{position:absolute;left:39px;top:89px;font-size:14.4px;color:var(--lead-text)}
  .content .copy{position:absolute;left:48px;width:717px;font-size:14.2px;line-height:21.6px;color:var(--body-text);text-align:justify}

  .login{left:878px;top:606px;width:322px;height:258px;background:var(--panel-login)}
  .login h2{position:absolute;left:0;top:26px;width:322px;height:36px;padding-left:27px;line-height:36px;
    background:#12161c;font-family:"Open Sans",sans-serif;font-size:23px;font-weight:600;color:#fff}
  .field{position:absolute;left:41px;width:241px;height:28px;border-radius:3px;background:var(--field-bg);
    border:1px solid #9c9fa4;font-size:14px;color:var(--field-text);padding:5px 10px}
  .forgot{position:absolute;left:45px;top:172px;font-size:13px;color:#8d9198;text-decoration:underline}
  .btn{position:absolute;top:209px;width:95px;height:27px;border-radius:3px;text-align:center;line-height:27px;
    background:linear-gradient(180deg,var(--orange-top),var(--orange-bottom));color:#fff;font-size:15px;border:1px solid #b44a00}

  .tutor-label{left:878px;top:888px;width:322px;text-align:center;font-size:14.5px;color:#fff}
  .tutor-btn{left:901px;top:922px;width:275px;height:47px;border-radius:3px;border:1px solid #b94800;
    background:linear-gradient(180deg,#ffb12e,var(--orange-bottom));text-align:center;line-height:45px;
    font-family:"Comfortaa",sans-serif;font-weight:700;font-size:28px;color:#fff;text-shadow:0 1px 2px rgba(0,0,0,.45)}

  .footer{left:0;top:1132px;width:1200px;height:68px;background:linear-gradient(180deg,var(--footer-bg),#2f3642);
    border-top:1px solid #4a5261;text-align:center;line-height:68px;font-size:14px;color:var(--footer-text)}
</style>
</head>
<body>
<div class="page">
  <div class="band abs"></div>

  <nav class="nav abs">
    <a class="home" href="#">Home</a>
    <a href="#" style="left:222px">About Us</a>
    <a href="#" style="left:395px">Solutions</a>
    <a href="#" style="left:563px">Services</a>
    <a href="#" style="left:737px">Contact us</a>
  </nav>

  <div class="logo abs"><span class="mark"></span><span class="name">Varnex Tek Inc.</span></div>

  <div class="search abs">Search</div>
  <svg class="search-icon abs" width="30" height="30" viewBox="0 0 30 30" aria-label="Search">
    <circle cx="17" cy="11" r="7" fill="none" stroke="#c9ccd0" stroke-width="3"/>
    <line x1="12" y1="16" x2="4" y2="25" stroke="#c9ccd0" stroke-width="4" stroke-linecap="round"/>
  </svg>

  <span class="social abs" style="left:941px;background:#3b5ea8"></span>
  <span class="social abs" style="left:989px;background:#4cbbe9"></span>
  <span class="social abs" style="left:1037px;background:#f2841c"></span>

  <div class="slider abs">
    <div class="slide" role="img" aria-label="Service slide photo: a student and a tutor each working at a computer in a classroom">
      <div class="half left"></div>
      <div class="half right"></div>
    </div>
  </div>

  <section class="content abs">
    <svg class="bullet" width="24" height="24" viewBox="0 0 24 24">
      <circle cx="12" cy="12" r="10" fill="none" stroke="#3fe0ee" stroke-width="2.5"/>
      <path d="M7 12h8M12 8l4 4-4 4" fill="none" stroke="#3fe0ee" stroke-width="2.5"/>
    </svg>
    <h1>Lorem Ipsum</h1>
    <p class="lead">It is a long established fact that a reader will be distracted by</p>
    <p class="copy" style="top:138px">It is a long established fact that a reader will be distracted by the readable content of a page when looking at its layout. The point of using Lorem Ipsum is that it has a more-or-less normal distribution of letters, as opposed to using 'Content here, content here', making it look like readable English. Many desktop publishing packages and web page editors now use Lorem Ipsum as their default model text, and a search for 'lorem ipsum' will uncover many web sites still in their infancy. Various versions have evolved over the years, sometimes by accident, sometimes on purpose (injected humour and the like).</p>
    <p class="copy" style="top:294px">It is a long established fact that a reader will be distracted by the readable content of a page when looking at its layout. The point of using Lorem Ipsum is that it has a more-or-less normal distribution of letters, as opposed to using 'Content here, content here', making it look like readable English. Many desktop publishing packages and web page editors now use Lorem Ipsum as their default model text, and a search for 'lorem ipsum' will uncover many web sites still in their infancy. Various versions have evolved over the years, sometimes by accident, sometimes on purpose (injected humour and the like).</p>
  </section>

  <aside class="login abs">
    <h2>Log In</h2>
    <div class="field" style="top:90px">User Name</div>
    <div class="field" style="top:138px">Pasword</div>
    <span class="forgot">Forgot pasword ?</span>
    <span class="btn" style="left:65px">Sign in</span>
    <span class="btn" style="left:173px">Sign up</span>
  </aside>

  <p class="tutor-label abs">Click Here For Online Tutoring</p>
  <div class="tutor-btn abs">Online Tutoring</div>

  <footer class="footer abs">All copyrights © received Varnex Tek Inc.</footer>
</div>
</body>
</html>
```